New Website design for VelvetCrate.com - A Monthly Subscription Sexy Lingerie Biz

Look at these sites: https://www.quillrazorguild.com; http://www.parcelwardrobe.com; http://www.tinyfernpack.com; https://www.ochreladle.com; https://thegoldenradish.com; http://www.petalwickcrate.com; https://wagtote.com; https://www.marlowehush.com/coral

Industry/Entity Type

Lingerie

Coding

Coded - Design and coding required

Number of Pages Required

1 page

```html
<!DOCTYPE html>
<html lang="en">
<head>
<meta charset="utf-8">
<title>VelvetCrate – Monthly Lingerie Subscription</title>
<link href="https://fonts.googleapis.com/css2?family=Raleway:wght@200;300;400;600&family=Open+Sans:ital,wght@0,400;0,600;1,400&display=swap" rel="stylesheet">
<style>
:root{
  --pink:#f7496b;
  --pink-deep:#f13a5e;
  --dark:#222222;
  --footer:#3a3a3a;
  --footer-line:#555555;
  --ink:#333333;
  --grey-text:#666666;
  --light-band:#f6f6f6;
  --sub-band:#e6e6e6;
  --white:#ffffff;
}
*{margin:0;padding:0;box-sizing:border-box}
html,body{width:1200px;height:3066px;overflow:hidden;background:var(--white)}
body{position:relative;font-family:"Open Sans",Arial,sans-serif;color:var(--ink)}
.abs{position:absolute}
.heading{font-family:"Raleway",Helvetica,sans-serif;font-weight:300;text-transform:uppercase;letter-spacing:1px}

/* nav */
.site-nav{left:0;top:0;width:1200px;height:64px;background:var(--dark)}
.brand{left:161px;top:18px;font-family:"Raleway",sans-serif;font-size:22px;font-weight:400;color:var(--white);letter-spacing:.5px}
.menu{left:432px;top:25px;display:flex;font-size:11px;color:var(--white);letter-spacing:.5px}
.menu span{margin-right:42px}
.btn-signup{left:897px;top:16px;width:72px;height:32px;border:1px solid #bbb;color:var(--white);font-size:10px;line-height:30px;text-align:center;border-radius:2px}
.btn-login{left:979px;top:16px;width:58px;height:32px;background:var(--pink);color:var(--white);font-size:10px;line-height:32px;text-align:center;border-radius:2px}

/* hero */
.hero{left:0;top:64px;width:1200px;height:526px;background:linear-gradient(120deg,#8c847c 0%,#b8aea3 35%,#5d5753 60%,#a79c8e 100%)}
.hero-shade{left:0;top:64px;width:1200px;height:526px;background:rgba(0,0,0,.28)}
.hero-title{left:0;top:226px;width:1200px;text-align:center;font-size:50px;color:var(--white);letter-spacing:2px}
.hero-sub{left:250px;top:300px;width:700px;text-align:center;font-size:21px;line-height:32px;color:var(--white)}
.btn-hero{left:519px;top:395px;width:160px;height:47px;background:var(--pink);color:var(--white);font-size:15px;font-weight:600;line-height:47px;text-align:center;letter-spacing:1px;border-radius:2px}
.dots{left:554px;top:523px;display:flex;gap:4px}
.dots i{display:block;width:14px;height:14px;border-radius:50%;background:rgba(255,255,255,.5)}
.dots i.on{background:var(--white)}

/* how it works */
.section-title{left:0;width:1200px;text-align:center;font-size:33px;color:#444}
.step-ring{width:114px;height:114px;border-radius:50%;border:2px solid var(--pink)}
.step-ring::after{content:"";position:absolute;left:8px;top:8px;width:94px;height:94px;border-radius:50%;border:1px solid var(--pink)}
.step-num{width:114px;line-height:110px;text-align:center;font-family:"Raleway",sans-serif;font-weight:200;font-size:44px;color:var(--pink)}
.step-label{width:300px;text-align:center;font-size:24px;color:#555}
.step-text{width:260px;text-align:center;font-size:13px;line-height:22px;color:#444}

/* feature bands */
.band-light{left:0;width:1200px;background:var(--light-band)}
.feature-kicker{font-size:37px;color:#555}
.feature-big{font-size:64px;color:#555;font-weight:200;letter-spacing:2px}
.feature-copy{width:420px;font-size:12.5px;line-height:22px;color:#444}
.feature-copy p{margin-bottom:20px}

/* testimonials */
.reviews{left:0;top:1419px;width:1200px;height:364px;background:linear-gradient(120deg,#f85a76,var(--pink) 45%,#f03f61)}
.reviews-title{left:0;top:1458px;width:1200px;text-align:center;font-size:32px;color:rgba(255,255,255,.85)}
.avatar{width:156px;height:156px;border-radius:50%;border:4px solid var(--white);background:linear-gradient(135deg,#e8c9b8,#b9877a)}
.quote{width:242px;font-size:11.5px;line-height:21px;font-style:italic;color:var(--white);text-align:justify}
.quote b{font-family:Georgia,serif;font-size:26px;font-style:normal;line-height:0;vertical-align:-8px}
.reviewer{font-size:12px;color:var(--white)}
.arrow{font-size:28px;color:var(--white)}

/* gallery */
.gram-tile{width:160px;height:215px}
.gram-cap{width:160px;text-align:center;font-size:11.5px;line-height:17px;color:#555}

/* subscribe */
.subscribe{left:0;top:2629px;width:1200px;height:194px;background:var(--sub-band)}
.sub-copy{left:161px;top:2682px;font-size:29px;line-height:52px;color:#555;letter-spacing:.5px}
.field{left:591px;width:331px;height:41px;background:var(--white);font-size:13px;font-style:italic;color:#777;line-height:41px;padding-left:12px}
.btn-round{left:942px;top:2688px;width:98px;height:98px;border-radius:50%;background:var(--pink);color:var(--white);text-align:center;font-size:13px;font-weight:600;padding-top:30px;line-height:19px}
.btn-round span{font-size:18px}

/* footer */
.site-footer{left:0;top:2823px;width:1200px;height:243px;background:var(--footer)}
.foot-col{top:2851px;color:var(--white);font-size:11px;line-height:20px}
.foot-col h4{font-size:11.5px;font-weight:600;letter-spacing:1px;margin-bottom:16px}
.foot-input{left:767px;top:2888px;width:271px;height:35px;background:var(--white);font-size:11px;color:#777;line-height:35px;padding-left:10px}
.foot-btn{left:767px;top:2929px;width:102px;height:37px;background:var(--pink);color:var(--white);font-size:11px;font-weight:600;line-height:37px;text-align:center}
.foot-rule{left:161px;top:2999px;width:878px;height:1px;background:var(--footer-line)}
.copyright{left:161px;top:3023px;font-size:10.5px;color:#ddd}
.social{top:3016px;display:flex;gap:4px;left:904px}
.social i{display:block;width:30px;height:30px;border-radius:50%;border:2px solid var(--white)}
.page-tag{left:1062px;top:3024px;font-size:10px;color:#ddd}
</style>
</head>
<body>

<header class="abs site-nav"></header>
<div class="abs brand">VELVETCRATE</div>
<nav class="abs menu"><span>ABOUT US</span><span>HOW IT WORKS</span><span>OFFICE BOX</span><span>ABOUT</span><span>SHOP</span></nav>
<div class="abs btn-signup">SIGN UP</div>
<div class="abs btn-login">LOGIN</div>

<div class="abs hero" role="img" aria-label="Photo of a model in black lace lingerie reclining on a vintage sofa"></div>
<div class="abs hero-shade"></div>
<h1 class="abs heading hero-title">Everyday Essentials</h1>
<p class="abs hero-sub">Sed ut perspiciatis unde omnis iste natus error sit voluptatem accusantium doloremque lauda ntium, tota aperiam</p>
<div class="abs btn-hero">GET YOUR BOX</div>
<div class="abs dots"><i></i><i></i><i class="on"></i><i></i><i></i></div>

<h2 class="abs heading section-title" style="top:622px">How VelvetCrate Works</h2>
<div class="abs step-ring" style="left:231px;top:712px"></div>
<div class="abs step-num" style="left:231px;top:712px">01</div>
<div class="abs step-ring" style="left:544px;top:712px"></div>
<div class="abs step-num" style="left:544px;top:712px">02</div>
<div class="abs step-ring" style="left:857px;top:712px"></div>
<div class="abs step-num" style="left:857px;top:712px">03</div>
<svg class="abs" style="left:370px;top:730px" width="160" height="60" viewBox="0 0 160 60" aria-hidden="true">
  <path d="M8 40 Q70 -5 150 35" fill="none" stroke="#888" stroke-width="1.5" stroke-dasharray="5 5"/>
  <path d="M140 27 L152 36 L138 40" fill="none" stroke="#888" stroke-width="1.5"/>
</svg>
<svg class="abs" style="left:690px;top:740px" width="160" height="60" viewBox="0 0 160 60" aria-hidden="true">
  <path d="M8 20 Q70 70 145 28" fill="none" stroke="#888" stroke-width="1.5" stroke-dasharray="5 5"/>
  <path d="M133 24 L147 27 L140 39" fill="none" stroke="#888" stroke-width="1.5"/>
</svg>
<div class="abs heading step-label" style="left:138px;top:838px">Sign-Up</div>
<div class="abs heading step-label" style="left:451px;top:838px">Size</div>
<div class="abs heading step-label" style="left:764px;top:838px">Enjoy</div>
<p class="abs step-text" style="left:158px;top:880px">Sed ut perspiciatis unde omnis iste natus orsit voluptatem accusantium doloremque laudantium, totam rem aperieaque.</p>
<p class="abs step-text" style="left:471px;top:880px">Sed ut perspiciatis unde omnis iste natus orsit voluptatem accusantium doloremque laudantium, totam rem aperieaque.</p>
<p class="abs step-text" style="left:784px;top:880px">Sed ut perspiciatis unde omnis iste natus orsit voluptatem accusantium doloremque laudantium, totam rem aperieaque.</p>

<section class="abs band-light" style="top:1004px;height:415px"></section>
<div class="abs" style="left:527px;top:1004px;width:673px;height:415px;clip-path:polygon(0 0,100% 0,100% 100%,22% 100%);background:linear-gradient(120deg,#f4f2f0,#e3d8d3 40%,#c6a79f 70%,#7d6763)" role="img" aria-label="Photo of a model in floral lace lingerie beside a vase of roses in a white room"></div>
<div class="abs heading feature-kicker" style="left:156px;top:1052px">The Fashion</div>
<div class="abs heading feature-big" style="left:154px;top:1098px">Trending</div>
<div class="abs feature-copy" style="left:161px;top:1196px">
  <p>Sed ut perspiciatis unde omnis iste natus error sit voluptatem accusantium doloremque laudantium, totam rem aperiam, eaque ipsa quae ab illo inventore veritatis et quasi architecto beatae vitae dicta sunt explicabo.</p>
  <p>Nemo enim ipsam voluptatem quia voluptas sit aspernaturodit aut fugit, sed quia consequuntur magni dolores eos qui ratione voluptatem sequi nesciuneque porro quisquam.</p>
</div>

<section class="abs reviews"></section>
<h2 class="abs heading reviews-title">People Are Loving This Idea</h2>
<div class="abs arrow" style="left:106px;top:1616px">&#8249;</div>
<div class="abs arrow" style="left:1090px;top:1616px">&#8250;</div>
<div class="abs avatar" style="left:163px;top:1557px" role="img" aria-label="Portrait of a customer"></div>
<p class="abs quote" style="left:333px;top:1542px"><b>&ldquo;</b> Sed ut perspiciatis unde omnis iste natus error sit voluptatem accusantium doloremque laudantium, totam rem aperiam, eaque ipsa quae ab illo inven tore veritatis et quasi architecto beatae vitae dicta sunt explicabo. <b>&rdquo;</b></p>
<div class="abs reviewer" style="left:338px;top:1692px">ROSA LANE, CITY NAME</div>
<div class="abs avatar" style="left:627px;top:1557px" role="img" aria-label="Portrait of a customer"></div>
<p class="abs quote" style="left:797px;top:1542px"><b>&ldquo;</b> Sed ut perspiciatis unde omnis iste natus error sit voluptatem accusantium dolore mque laudantium, totam rem aperiam, eaque ipsa quae ab illo inven tore veritatis et quasi architecto beatae vitae dicta sunt explicabo. <b>&rdquo;</b></p>
<div class="abs reviewer" style="left:802px;top:1692px">ROSA LANE, CITY NAME</div>

<section class="abs band-light" style="top:1785px;height:412px"></section>
<div class="abs" style="left:0;top:1785px;width:624px;height:412px;clip-path:polygon(0 0,100% 0,74% 100%,0 100%);background:linear-gradient(130deg,#d8c8bd,#f2ebe6 45%,#bba293 80%,#8c7264)" role="img" aria-label="Photo of a model in white lingerie lying on a bed"></div>
<div class="abs heading feature-kicker" style="left:626px;top:1831px">Our Top</div>
<div class="abs heading feature-big" style="left:624px;top:1876px">Brands</div>
<div class="abs feature-copy" style="left:634px;top:1976px">
  <p>Sed ut perspiciatis unde omnis iste natus error sit voluptatem accusantium doloremque laudantium, totam rem aperiam, eaque ipsa quae ab illo inventore veritatis et quasi architecto beatae vitae dicta sunt explicabo.</p>
  <p>Nemo enim ipsam voluptatem quia voluptas sit aspernaturodit aut fugit, sed quia consequuntur magni dolores eos qui ratione voluptatem sequi nesciuneque porro quisquam.</p>
</div>

<h2 class="abs heading section-title" style="top:2258px">VelvetCrate @ PhotoNest</h2>
<div class="abs gram-tile" style="left:161px;top:2328px;background:linear-gradient(160deg,#c4202c,#8e1018)" role="img" aria-label="Photo of a model in red lingerie"></div>
<div class="abs gram-tile" style="left:341px;top:2328px;background:linear-gradient(160deg,#9fb2b5,#d8c2b3 55%,#6d7573)" role="img" aria-label="Photo of a model in a red bikini by the sea"></div>
<div class="abs gram-tile" style="left:521px;top:2328px;background:linear-gradient(160deg,#3a3533,#1a1717 60%,#4a403c)" role="img" aria-label="Photo of a model in black lingerie"></div>
<div class="abs gram-tile" style="left:701px;top:2328px;background:linear-gradient(160deg,#5b4740,#c79b84 55%,#2a2222)" role="img" aria-label="Photo of a model in a black bra set"></div>
<div class="abs gram-tile" style="left:877px;top:2328px;background:linear-gradient(160deg,#cfe3ea,#8fd0cf 55%,#e8dcd2)" role="img" aria-label="Photo of a model in turquoise lingerie"></div>
<p class="abs gram-cap" style="left:161px;top:2551px">Neque ro quisquam quim est loprelorem ipsm.</p>
<p class="abs gram-cap" style="left:341px;top:2551px">Neque ro quisquam quim est loprelorem ipsm.</p>
<p class="abs gram-cap" style="left:521px;top:2551px">Neque ro quisquam quim est loprelorem ipsm.</p>
<p class="abs gram-cap" style="left:701px;top:2551px">Neque ro quisquam quim est loprelorem ipsm.</p>
<p class="abs gram-cap" style="left:877px;top:2551px">Neque ro quisquam quim est loprelorem ipsm.</p>

<section class="abs subscribe"></section>
<svg class="abs" style="left:572px;top:2629px" width="56" height="22" viewBox="0 0 56 22" aria-hidden="true"><path d="M0 0 H56 L28 22 Z" fill="#ffffff"/></svg>
<div class="abs heading sub-copy">Monthly Subscription<br>Sexy Lingerie Biz.</div>
<div class="abs field" style="top:2686px">Name</div>
<div class="abs field" style="top:2733px">Email</div>
<div class="abs btn-round">SUBSCRIBE<br><span>HERE</span></div>

<footer class="abs site-footer"></footer>
<div class="abs foot-col" style="left:161px"><h4>COMPANY</h4>Get a WagTote<br>Give a Gift<br>Claim a Gift<br>Get the App</div>
<div class="abs foot-col" style="left:325px"><h4>HELP</h4>Privacy Policy<br>Terms of Service<br>We're Hiring<br>Advertise</div>
<div class="abs foot-col" style="left:489px"><h4>SUPPORT</h4>Wishlist<br>Customer Care<br>Add To Cart</div>
<div class="abs foot-col" style="left:634px"><h4>LINKS</h4>About Us<br>Affiliates<br>Terms<br>Sitemap</div>
<div class="abs foot-col" style="left:767px"><h4>NEWSLETTER</h4></div>
<div class="abs foot-input">Email address</div>
<div class="abs foot-btn">SUBSCRIBE</div>
<div class="abs foot-rule"></div>
<div class="abs copyright">&copy; 2016 VelvetCrate. All right reserved &nbsp;Term of Use</div>
<div class="abs social" aria-label="Social links"><i></i><i></i><i></i><i></i></div>
<div class="abs page-tag">c4</div>

</body>
</html>
```